we are a mobile auto windscreen replacement business we are looking for a smart, stylish designed card on a matte black base color with large metallic silver KVT (similar to the zenpod box)
over the whole face of the card but down the bottom have (your local automotive & machinery glass specialist) & over the back

Reason: I'm looking for a design like no other something that really wows people to grab a card & use my business

Target Market(s)

Adults in western countries that own an automotive fleet company or anybody that owns a car

Industry/Entity Type

Automotive

Contact Information for Business Card

front: KVTglassworks
Back: MORRIS 0482 65 71 93 Abn: 52840193657
morris@kvtglassworks.com.au & www.kvtglassworks.com.au

Logo styles of interest
Lettermark Logo
Requirements
Must have
• Metallic font on matte background
Nice to have
• 3D font that's glass or the word KVT smashed into glass on a black background I've added some pictures that maybe you could incorporate in the background or font it would be great to see a professionals ideas

```html
<!DOCTYPE html>
<html lang="en">
<head>
<meta charset="utf-8">
<title>KVT Glassworks – Business Card</title>
<link rel="stylesheet" href="https://fonts.googleapis.com/css2?family=Lato:wght@400;700&display=swap">
<style>
  :root {
    --canvas-bg: #e9e6e1;
    --card-black: #050505;
    --panel-black: #000000;
    --texture-dark: #1f1f21;
    --texture-mid: #3a3a3d;
    --silver: #c9cacc;
    --white: #ffffff;
    --soft-white: #d8d8d8;
    --muted: #9a9a9a;
  }
  * { margin: 0; padding: 0; box-sizing: border-box; }
  html, body {
    width: 1200px; height: 1000px; overflow: hidden;
    background: var(--canvas-bg);
    font-family: "Lato", Arial, sans-serif;
  }
  .canvas { position: relative; width: 1200px; height: 1000px; }

  .card {
    position: absolute; top: 350px;
    width: 537px; height: 300px;
    border-radius: 9px; overflow: hidden;
    box-shadow: 0 6px 16px rgba(0,0,0,0.35);
  }

  /* Front */
  .card-front { left: 45px; }
  .card-front .glass-texture {
    position: absolute; inset: 0;
    background: radial-gradient(ellipse at 50% 40%, var(--texture-mid), var(--texture-dark) 75%);
  }
  .card-front .logo-panel {
    position: absolute; left: 80px; top: 13px;
    width: 378px; height: 274px;
    border-radius: 10px;
    background: linear-gradient(125deg, #161616 0%, var(--panel-black) 45%, #0b0b0b 100%);
    display: flex; align-items: center; justify-content: center;
  }
  .card-front .brand-name {
    font-family: "Lato", Arial, sans-serif;
    font-weight: 700;
    font-size: 76px;
    letter-spacing: 2px;
    color: var(--silver);
    margin-top: 6px;
  }

  /* Back */
  .card-back { left: 617px; background: var(--card-black); }
  .card-back .holder-name {
    position: absolute; top: 62px; width: 100%;
    text-align: center;
    font-weight: 700; font-size: 23px; letter-spacing: 0.5px;
    color: var(--white);
  }
  .card-back .tagline {
    position: absolute; top: 138px; width: 100%;
    text-align: center;
    font-size: 16.5px; letter-spacing: 1.3px;
    color: var(--soft-white);
  }
  .card-back .contact-list {
    position: absolute; left: 30px; top: 186px;
    list-style: none;
  }
  .card-back .contact-item {
    display: flex; align-items: center; gap: 8px;
    height: 28px;
    font-size: 15px; color: var(--white);
  }
  .card-back .contact-icon { width: 19px; height: 19px; flex: none; }
  .card-back .abn {
    position: absolute; right: 30px; top: 248px;
    font-size: 12px; color: var(--muted);
  }
</style>
</head>
<body>
<main class="canvas">

  <section class="card card-front" aria-label="Card front">
    <div class="glass-texture" role="img" aria-label="Dark cracked glass texture background"></div>
    <div class="logo-panel">
      <span class="brand-name">KVT</span>
    </div>
  </section>

  <section class="card card-back" aria-label="Card back">
    <h1 class="holder-name">MORRIS</h1>
    <p class="tagline">Your Local Automotive &amp; Machinery Glass Specialist</p>
    <ul class="contact-list">
      <li class="contact-item">
        <svg class="contact-icon" viewBox="0 0 20 20" aria-hidden="true">
          <circle cx="10" cy="10" r="9" fill="none" stroke="#fff" stroke-width="1.5"/>
          <path d="M6.3 5.5c.6-.6 1.3-.5 1.6 0l1 1.6c.3.5.2 1-.2 1.3l-.6.5c.5 1.2 1.5 2.2 2.7 2.8l.5-.6c.4-.4.9-.5 1.3-.2l1.6 1c.5.3.6 1 0 1.6l-.6.6c-.8.8-2.6.4-4.5-1.3S4.9 7.4 5.7 6.1z" fill="#fff"/>
        </svg>
        <span>0482 65 71 93</span>
      </li>
      <li class="contact-item">
        <svg class="contact-icon" viewBox="0 0 20 20" aria-hidden="true">
          <circle cx="10" cy="10" r="9" fill="none" stroke="#fff" stroke-width="1.5"/>
          <circle cx="10" cy="10" r="2.6" fill="none" stroke="#fff" stroke-width="1.5"/>
          <path d="M12.6 7.5v3.3c0 1.2 1.8 1.3 1.8-.3A4.5 4.5 0 1 0 12 14" fill="none" stroke="#fff" stroke-width="1.5"/>
        </svg>
        <span>morris@kvtglassworks.com.au</span>
      </li>
      <li class="contact-item">
        <svg class="contact-icon" viewBox="0 0 20 20" aria-hidden="true">
          <circle cx="10" cy="10" r="9" fill="#fff"/>
          <g fill="none" stroke="#000" stroke-width="1">
            <circle cx="10" cy="10" r="6"/>
            <ellipse cx="10" cy="10" rx="2.6" ry="6"/>
            <path d="M4 10h12M5 7h10M5 13h10"/>
          </g>
        </svg>
        <span>www.kvtglassworks.com.au</span>
      </li>
    </ul>
    <p class="abn">Abn: 52840193657</p>
  </section>

</main>
</body>
</html>
```